The Deskwell (A new and exciting small Business support solution) Business Cards

The Deskwell Business Card Design

About us:
The Deskwell is a small business support solution, assisting businesses with any marketing, office management and human resource skills.

Objective
To be a small business lifesaver, to relieve busy professionals from mundane operations so they can focus on their businesses future through complete, reliable, efficient and effective client support. To have people say WOW what did we do before The Deskwell.

Industry/Entity Type

Small Business

Colors
0355a3
33a6d7

Requirements
Must have
• Must be similar to the look and feel of my website http://www.thedeskwell-example.com.au/

Must have:

Blue colour is 0094FF

The Logo

A Small Business Support Solution
- Human Resources
- Office Administration
- Marketing

Maribel Torvik
0462 837 105
maribeltorvik@thedeskwell-example.com.au
www.thedeskwell-example.com

```html
<!DOCTYPE html>
<html lang="en">
<head>
<meta charset="utf-8">
<title>The Deskwell – Business Cards</title>
<link href="https://fonts.googleapis.com/css2?family=Open+Sans:ital,wght@0,400;0,600;0,700;1,700&display=swap" rel="stylesheet">
<style>
  :root {
    --brand-blue: #1a94d2;
    --ink: #111111;
    --paper: #ffffff;
    --backdrop: #9a9a9a;
    --card-shadow: rgba(0, 0, 0, 0.28);
  }
  html, body {
    margin: 0;
    padding: 0;
    width: 1200px;
    height: 900px;
    overflow: hidden;
  }
  body {
    background: var(--backdrop);
    font-family: "Open Sans", Arial, sans-serif;
    color: var(--ink);
    position: relative;
  }
  .card {
    position: absolute;
    width: 560px;
    height: 330px;
    box-sizing: border-box;
    box-shadow: 0 6px 18px var(--card-shadow);
  }
  .card--front {
    left: 70px;
    top: 80px;
    background: var(--brand-blue);
    display: flex;
    align-items: center;
    justify-content: center;
  }
  .card--front .wordmark {
    color: var(--paper);
    font-size: 58px;
  }
  .wordmark {
    font-weight: 400;
    letter-spacing: -0.5px;
    margin: 0;
    line-height: 1;
  }
  .card--back {
    left: 570px;
    top: 490px;
    background: var(--paper);
    padding: 26px 30px 0 34px;
  }
  .card--back .wordmark {
    color: var(--ink);
    font-size: 46px;
  }
  .holder {
    margin: 34px 0 0 58px;
  }
  .holder__name {
    margin: 0;
    color: var(--brand-blue);
    font-weight: 700;
    font-style: italic;
    font-size: 15px;
    text-transform: uppercase;
    letter-spacing: 0.4px;
  }
  .holder__role {
    margin: 0;
    font-size: 11px;
  }
  .details {
    position: absolute;
    left: 0;
    right: 0;
    top: 238px;
    display: flex;
    justify-content: space-between;
    padding-right: 34px;
  }
  .detail-block {
    border-left: 6px solid var(--brand-blue);
    padding-left: 12px;
    font-size: 11.5px;
    line-height: 1.45;
  }
  .detail-block p { margin: 0; }
  .detail-block--contact { margin-left: 14px; }
  .detail-block--services { margin-top: 0; }
</style>
</head>
<body>
  <section class="card card--front" aria-label="Business card front">
    <h1 class="wordmark">The Deskwell</h1>
  </section>

  <section class="card card--back" aria-label="Business card back">
    <h2 class="wordmark">The Deskwell</h2>
    <div class="holder">
      <p class="holder__name">Maribel Torvik</p>
      <p class="holder__role">Director</p>
    </div>
    <div class="details">
      <div class="detail-block detail-block--contact">
        <p>0462 837 105</p>
        <p>maribeltorvik@thedeskwell-example.com.au</p>
        <p>www.thedeskwell-example.com.au</p>
      </div>
      <div class="detail-block detail-block--services">
        <p>A Small Business Support Solution</p>
        <p>Human Resources</p>
        <p>Office Administration</p>
        <p>Marketing</p>
      </div>
    </div>
  </section>
</body>
</html>
```